Business Cards

Simple but professional looking business cards

Name: Rina Toskovar
Title: Principal Enterprise Systems Consultant
Email: r@kldo.net.au
web : www.kldo.net.au
Phone: +61.8.92315547
Mobile: +61.438516622

Hi All, Please include the office address Level 3, 48 Bramwell St, Corran Heights, QL, 7214

```html
<!DOCTYPE html>
<html lang="en">
<head>
<meta charset="utf-8">
<title>KLDO Business Cards</title>
<link rel="stylesheet" href="https://fonts.googleapis.com/css2?family=Questrial&display=swap">
<style>
  :root {
    --page: #e9e6e2;
    --blue-light: #1ba0da;
    --blue-deep: #0a74bf;
    --band: #000000;
    --white: #ffffff;
    --ink: #0b0b0b;
    --icon-cut: #1a92d2;
  }
  * { box-sizing: border-box; margin: 0; padding: 0; }
  html, body { width: 1200px; height: 914px; overflow: hidden; }
  body {
    background: var(--page);
    font-family: "Questrial", "Century Gothic", sans-serif;
    position: relative;
  }
  .card {
    position: absolute;
    left: 250px;
    width: 700px;
    height: 400px;
    background: linear-gradient(135deg, var(--blue-light) 0%, var(--blue-deep) 100%);
    box-shadow: 0 6px 18px rgba(0,0,0,0.18);
    overflow: hidden;
  }
  .card-front { top: 47px; }
  .card-back { top: 467px; }

  .brand {
    position: absolute;
    display: flex;
    align-items: center;
    color: var(--white);
    letter-spacing: 2px;
    white-space: nowrap;
  }
  .brand-dot {
    border-radius: 50%;
    border: 5px solid var(--white);
  }
  .card-front .brand { left: 50%; top: 50%; transform: translate(-50%, -50%); font-size: 92px; gap: 22px; }
  .card-front .brand-dot { width: 70px; height: 70px; }
  .card-back .brand { left: 50%; top: 38px; transform: translateX(-50%); font-size: 48px; gap: 12px; }
  .card-back .brand-dot { width: 38px; height: 38px; border-width: 3px; }

  .name-band {
    position: absolute;
    left: 0; right: 0; top: 138px;
    height: 54px;
    border-top: 3px solid var(--white);
    border-bottom: 3px solid var(--white);
    background: var(--band);
    box-shadow: inset 0 0 0 3px var(--blue-deep);
    display: flex;
    align-items: center;
    justify-content: space-between;
    padding: 0 36px 0 50px;
    color: var(--white);
    white-space: nowrap;
  }
  .person-name { font-size: 24px; }
  .person-title { font-size: 18px; }

  .contact-list {
    position: absolute;
    list-style: none;
    color: var(--ink);
    font-size: 20px;
    line-height: 30px;
    white-space: nowrap;
  }
  .contact-list li { display: flex; align-items: flex-start; gap: 14px; }
  .contact-list svg { width: 16px; height: 16px; flex: none; margin-top: 7px; fill: var(--ink); }
  .contact-personal { left: 58px; top: 228px; }
  .contact-office { left: 380px; top: 250px; }

  .divider {
    position: absolute;
    left: 345px; top: 240px;
    width: 3px; height: 100px;
    background: var(--white);
  }
</style>
</head>
<body>

<section class="card card-front" aria-label="Card front">
  <div class="brand"><span class="brand-dot"></span><span class="brand-name">KLDO</span></div>
</section>

<section class="card card-back" aria-label="Card back">
  <div class="brand"><span class="brand-dot"></span><span class="brand-name">KLDO</span></div>

  <div class="name-band">
    <span class="person-name">Rina Toskovar</span>
    <span class="person-title">Principal Enterprise Systems Consultant</span>
  </div>

  <ul class="contact-list contact-personal">
    <li>
      <svg viewBox="0 0 16 16" aria-hidden="true"><rect x="4" y="0" width="8" height="16" rx="1.5"/><rect x="5.5" y="2" width="5" height="7" fill="var(--icon-cut)"/></svg>
      <span>+61.438516622</span>
    </li>
    <li>
      <svg viewBox="0 0 16 16" aria-hidden="true"><path d="M1 5 Q8 0 15 5 L13 7 L11 5 L5 5 L3 7 Z"/><rect x="3" y="8" width="10" height="7" rx="1"/></svg>
      <span>+61.8.92315547</span>
    </li>
    <li>
      <svg viewBox="0 0 16 16" aria-hidden="true"><rect x="0" y="3" width="16" height="11"/><path d="M0 3 L8 9 L16 3" fill="none" stroke="var(--icon-cut)" stroke-width="1.4"/></svg>
      <span>r@kldo.net.au</span>
    </li>
  </ul>

  <div class="divider"></div>

  <ul class="contact-list contact-office">
    <li>
      <svg viewBox="0 0 16 16" aria-hidden="true"><circle cx="8" cy="8" r="8"/><path d="M0 8 H16 M8 0 V16 M3 3 Q8 6 13 3 M3 13 Q8 10 13 13" stroke="var(--icon-cut)" stroke-width="1" fill="none"/></svg>
      <span>www.kldo.net.au</span>
    </li>
    <li>
      <svg viewBox="0 0 16 16" aria-hidden="true"><path d="M8 0 A5.5 5.5 0 0 1 13.5 5.5 C13.5 9 8 16 8 16 C8 16 2.5 9 2.5 5.5 A5.5 5.5 0 0 1 8 0 Z"/><circle cx="8" cy="5.5" r="2" fill="var(--icon-cut)"/></svg>
      <span>Level 3, 48 Bramwell St,<br>Corran Heights, QL, 7214</span>
    </li>
  </ul>
</section>

</body>
</html>
```